Holiday Graphic for Cover of Catalog

We're looking for a design that represents the Holiday season to use on the cover of this year's holiday catalog. You can take a look at 2011's catalog at this link: http://pagroven.net/tindervale/docs/holiday_gift_guide. Your design should not be a replication, but it can be inspired by the cover of 2011's Catalog.

Please create a design that is WINTER-specific, not necessarily Christmas, Hanukkah, or any other holiday-specific design. Something simple, modern, contemporary is preferable. The design should have a specific color scheme & that scheme should be easily detectable by a viewer.

Options for The final size of the front-cover:
a. 8.5"width x 5.405"height
b. 8.5"width x 10.81"height
c. 10.81"height x 8.5"width
d. square 8.5" x 8.5"
Updates

Please note: I do not have the time or budget to have these printed with foil stamping, so please avoid any metallic finishes.  

Thanks!
Joan

Requirements
Must have
• Our logo, attached file.
• Title: "2013 Holiday Gift Giving Guide"

```html
<!DOCTYPE html>
<html lang="en">
<head>
<meta charset="utf-8">
<title>2013 Holiday Gift Giving Guide</title>
<link rel="stylesheet" href="https://fonts.googleapis.com/css2?family=Bodoni+Moda:opsz,wght@6..96,400&display=swap">
<style>
  :root {
    --sky: #4fd6ff;
    --frost: #82fff0;
    --ice: #00ffff;
    --snow: #ffffff;
  }
  html, body {
    margin: 0;
    padding: 0;
    width: 1078px;
    height: 1200px;
    overflow: hidden;
    background: var(--snow);
  }
  .cover {
    display: block;
    width: 1078px;
    height: 1200px;
  }
  .cover-band { fill: var(--sky); }
  .frost-facet { fill: var(--frost); }
  .ice-drop { fill: var(--ice); }
  .year-digit {
    font-family: "Bodoni Moda", "Didot", serif;
    font-size: 200px;
    text-anchor: middle;
  }
  .year-on-paper .year-digit { fill: var(--sky); }
  .year-on-band .year-digit { fill: var(--snow); }
  .title {
    font-family: "Bodoni Moda", "Didot", serif;
    fill: var(--snow);
  }
  .title-main { font-size: 102px; }
  .title-sub { font-size: 42px; }
</style>
</head>
<body>
<svg class="cover" viewBox="0 0 800 890" preserveAspectRatio="none" xmlns="http://www.w3.org/2000/svg" aria-labelledby="cover-title">
  <title id="cover-title">2013 Holiday Gift Giving Guide</title>
  <defs>
    <path id="band-shape" d="M95 10 L612 10 L612 145 C520 330 420 600 400 790 L305 790 C290 600 180 410 100 290 C40 200 20 80 95 10 Z"/>
    <clipPath id="band-clip">
      <use href="#band-shape"/>
    </clipPath>
    <radialGradient id="flake-glow" cx="50%" cy="50%" r="50%">
      <stop offset="0%" stop-color="#ffffff"/>
      <stop offset="70%" stop-color="#e6f9ff"/>
      <stop offset="100%" stop-color="#bff0ff" stop-opacity="0"/>
    </radialGradient>
  </defs>

  <use class="cover-band" href="#band-shape"/>

  <polygon class="frost-facet" points="10,10 72,10 38,120 30,175"/>
  <polygon class="frost-facet" points="58,220 108,300 108,372 70,372"/>
  <polygon class="frost-facet" points="0,620 0,790 112,790"/>
  <path class="ice-drop" d="M170 790 C170 745 182 718 200 720 C220 724 238 765 248 790 Z"/>

  <g class="year" aria-label="2013">
    <g class="year-on-paper">
      <text class="year-digit" x="57" y="166">2</text>
      <text class="year-digit" x="57" y="370">0</text>
      <text class="year-digit" x="57" y="576">1</text>
      <text class="year-digit" x="57" y="780">3</text>
    </g>
    <g class="year-on-band" clip-path="url(#band-clip)" aria-hidden="true">
      <text class="year-digit" x="57" y="166">2</text>
      <text class="year-digit" x="57" y="370">0</text>
    </g>
  </g>

  <text class="title title-main" x="212" y="100">Holiday</text>
  <text class="title title-sub" x="214" y="158">Gift Giving Guide</text>

  <circle class="snowflake" cx="530" cy="630" r="255" fill="url(#flake-glow)" role="img" aria-label="Large white snowflake with light blue outline and a small red star at its centre"/>
</svg>
</body>
</html>
```